A wedding company selling top 5 wedding venues in an affluent historic Florida Town

We need a word press design (Layered PSD files) to hand over to a web developer.
It's for Maple Hollow Nuptial Company. The company has been set up to sell wedding packages to the top 5 or so wedding venues in Winter Park. Winter Park is an historic Florida town which is known for it's European village feel, with paved roads and sidewalk seating for cafe's and restaurants.
Needs to be clean and fresh with an elegant feel.
We have a logo already established which you will find attached to the brief along with a few wedding photo's from a couple of the venues we will be selling.
We are starting with 4 venues, which will each have about 3 different packages. I'd like a design for a home page and an inside page.
We will have a blog, recent weddings page which we will update with photo's etc.
The home page will have tabs for:
Wedding Venues, Reception Venues, About US, Contact US, Blog,

Target Market(s)

Brides and Grooms looking for a stylish elegant wedding. Based in western speaking countries, aged between 20 - 50 years old. Probably more aimed at the female who makes the decisions.

Industry/Entity Type

Wedding

Font styles to use
Sans Serif

Colors

Designer to choose colors to be used in the design.

Requirements
Must have
• On the home page I'd like a big slider, A block with a paragraph about Winter Park in general, a twitter feed, a recent weddings link and a big button on each page which goes to a "request info" form.

```html
<!DOCTYPE html>
<html lang="en">
<head>
<meta charset="utf-8">
<title>Maple Hollow Nuptial Company</title>
<link href="https://fonts.googleapis.com/css2?family=Varela+Round&family=Open+Sans:wght@400;600&family=Libre+Baskerville&display=swap" rel="stylesheet">
<style>
:root{
  --purple:#5b2a9a;
  --purple-dark:#3d1a72;
  --magenta:#a8359f;
  --magenta-tab:#b444b4;
  --heading:#9b2d8f;
  --teal:#2f8db3;
  --text:#555;
  --text-dark:#333;
  --panel:#efefef;
  --panel-light:#f4f4f4;
  --line:#dcdcdc;
  --footer:#252525;
  --footer-text:#9a9a9a;
}
*{margin:0;padding:0;box-sizing:border-box}
html,body{width:734px;height:1200px;overflow:hidden;background:#fff}
body{position:relative;font-family:"Open Sans",sans-serif;color:var(--text)}
.abs{position:absolute}
.heading-font{font-family:"Varela Round",sans-serif}

/* header */
.brand{left:56px;top:34px;font-family:"Varela Round",sans-serif;font-size:17px;color:var(--purple);line-height:1.15;width:140px}
.call{right:54px;top:55px;text-align:right;color:var(--purple);font-family:"Varela Round",sans-serif}
.call small{display:block;font-size:11px}
.call strong{display:block;font-size:16px;font-weight:400;color:var(--magenta)}

/* nav */
.nav{left:0;top:97px;width:734px;height:33px;background:linear-gradient(var(--purple),var(--purple-dark))}
.nav a{position:absolute;top:0;height:33px;line-height:33px;text-align:center;color:#fff;font-family:"Varela Round",sans-serif;font-size:11.5px;text-decoration:none;border-right:1px solid rgba(255,255,255,.15)}
.nav a.current{background:var(--magenta-tab)}

/* slider */
.slider{left:0;top:130px;width:734px;height:301px;background:linear-gradient(100deg,#a9716a 0%,#d8cfc8 30%,#eae6e0 48%,#7a5650 62%,#4c6a3a 85%,#35542a 100%)}
.caption{left:60px;top:253px;width:272px;height:80px;border-radius:10px;background:rgba(168,53,159,.85);color:#fff;font-family:"Libre Baskerville",serif;padding:18px 20px}
.caption h2{font-weight:400;font-size:19px;line-height:1.2}
.caption p{font-size:13px;margin-top:2px}
.dots{left:348px;top:414px;display:flex;gap:3px}
.dots span{width:10px;height:10px;border-radius:50%;background:#111}
.dots span:first-child{background:#fff}

/* welcome */
.welcome-title{left:0;top:458px;width:734px;text-align:center;font-size:20px;color:var(--heading)}
.welcome-text{left:92px;top:487px;width:560px;text-align:center;font-size:7.6px;line-height:13.4px;color:var(--text)}

/* recent weddings */
.recent{left:1px;top:566px;width:732px;height:241px;background:var(--panel-light);border:1px solid var(--line)}
.recent-title{left:0;top:584px;width:734px;text-align:center;font-size:17px;color:var(--heading)}
.wedding-photo{top:622px;width:154px;height:160px}

/* columns */
.col-title{top:836px;width:187px;text-align:center;font-size:15.5px}
.col-panel{top:860px;width:187px;height:175px;background:var(--panel)}
.tweet-card{left:81px;top:870px;width:174px;height:100px;background:#fff;border-radius:3px;padding:7px 10px;font-size:7.2px;line-height:11.2px;color:var(--text-dark)}
.tweet-card .handle{color:var(--teal);margin-bottom:6px}
.tweet-card .handle span{color:#888}
.tweet-card a{color:var(--teal);text-decoration:none}
.tweet-actions{left:89px;top:981px;font-size:7.2px;color:var(--teal);display:flex;gap:8px}
.compose{left:81px;top:1002px;width:174px;height:22px;background:#fff;border:1px solid var(--line);border-radius:2px;font-size:7px;color:#888;padding:6px 10px}
.blog-item{left:287px;width:170px;height:44px}
.blog-thumb{position:absolute;left:0;top:0;width:50px;height:40px;border:2px solid #fff;box-shadow:0 1px 2px rgba(0,0,0,.25)}
.blog-text{position:absolute;left:59px;top:-2px;width:110px;font-size:7.4px;line-height:10.4px;color:var(--text-dark);text-align:justify}
.blog-text time{display:block;color:#888;margin-top:5px}
.field{left:495px;width:164px;height:21px;background:#fff;border:1px solid var(--line);border-radius:3px;font-size:7px;color:#888;padding:5px 8px}
.submit{left:620px;top:1004px;width:38px;height:18px;background:#3a3a3a;border-radius:3px;color:#fff;font-size:6.5px;text-align:center;line-height:18px}

/* info bar */
.info{left:0;top:1056px;width:734px;height:56px;background:var(--panel-light)}
.info-item{top:1073px;font-size:7.4px;line-height:13px;color:var(--text)}
.info-icon{top:1076px}

/* footer */
.footer{left:0;top:1112px;width:734px;height:88px;background:var(--footer)}
.foot-link{top:1130px;font-size:7.8px;color:var(--footer-text)}
.foot-rule{left:64px;top:1156px;width:610px;height:1px;background:#3a3a3a}
.copyright{left:66px;top:1173px;font-size:7.8px;color:var(--footer-text)}
.social{top:1169px;width:18px;height:18px;border-radius:50%;background:#6c6c6c}
</style>
</head>
<body>

<header>
  <div class="abs brand">Maple Hollow Nuptial Company</div>
  <div class="abs call"><small>Call Us Today</small><strong>555.214.7730</strong></div>
</header>

<nav class="abs nav">
  <a class="current" style="left:62px;width:68px">Home</a>
  <a style="left:130px;width:109px">Wedding Venues</a>
  <a style="left:239px;width:121px">Reception Venues</a>
  <a style="left:360px;width:79px">About Us</a>
  <a style="left:439px;width:101px">Photo &amp; Video</a>
  <a style="left:540px;width:90px">Contact Us</a>
  <a style="left:630px;width:48px;border-right:none">Blog</a>
</nav>

<section>
  <div class="abs slider" role="img" aria-label="Bride and groom standing in front of a brick archway with greenery"></div>
  <div class="abs caption">
    <h2>Book Wedding Packages</h2>
    <p>Duis quam Nam eget lacus</p>
  </div>
  <svg class="abs" style="left:28px;top:244px" width="28" height="66" viewBox="0 0 28 66"><polyline points="24,2 4,33 24,64" fill="none" stroke="#fff" stroke-width="1.5"/></svg>
  <svg class="abs" style="left:686px;top:244px" width="28" height="66" viewBox="0 0 28 66"><polyline points="4,2 24,33 4,64" fill="none" stroke="#fff" stroke-width="1.5"/></svg>
  <div class="abs dots"><span></span><span></span><span></span><span></span></div>
</section>

<section>
  <h1 class="abs welcome-title heading-font" style="font-weight:400">Welcome to Maple Hollow Wedding Mainpage</h1>
  <p class="abs welcome-text">Maecenas at justo id velit placerat molestie Donec dictum lectus non odio Cras a ante vitae enim iaculis aliquam Mauris nunc quam venenatis nec euismod sit amet egestas placerat est Pellentesque habitant morbi tristique senectus et netus et malesuada fames ac turpis egestas Cras id elit Integer quis urna Ut ante enim dapibus malesuada fringilla eu condimentum quis tellus Aenean porttitor eros vel dolor Donec convallis pede venenatis nibh Duis quam Nam eget lacus Aliquam erat volutpat Quisque dignissi</p>
</section>

<section>
  <div class="abs recent"></div>
  <h2 class="abs recent-title heading-font" style="font-weight:400">Recent weddings</h2>
  <div class="abs wedding-photo" style="left:126px;background:linear-gradient(90deg,#9a5a4a,#e8e4de 45%,#3a3e48 70%,#8a6a5a)" role="img" aria-label="Couple posing under a brick arch, bride holding a bouquet"></div>
  <div class="abs wedding-photo" style="left:295px;background:linear-gradient(180deg,#e6e2dc 0%,#d8d2ca 55%,#4a2a20 70%,#3a2018)" role="img" aria-label="Couple kissing in front of white curtains"></div>
  <div class="abs wedding-photo" style="left:463px;background:linear-gradient(90deg,#3a4a30,#e8e6e0 20%,#6a7a5a 50%,#8a5a4a 75%,#e4e2dc)" role="img" aria-label="Bride standing between white columns on a brick path"></div>
  <svg class="abs" style="left:86px;top:679px" width="12" height="18" viewBox="0 0 12 18"><polyline points="10,1 2,9 10,17" fill="none" stroke="#aaa" stroke-width="1.5"/></svg>
  <svg class="abs" style="left:646px;top:679px" width="12" height="18" viewBox="0 0 12 18"><polyline points="2,1 10,9 2,17" fill="none" stroke="#aaa" stroke-width="1.5"/></svg>
</section>

<section>
  <h3 class="abs col-title heading-font" style="left:68px;color:var(--teal);font-weight:400">Social Feeds</h3>
  <h3 class="abs col-title heading-font" style="left:279px;color:var(--purple-dark);font-weight:400">Latest Blog</h3>
  <h3 class="abs col-title heading-font" style="left:479px;color:var(--heading);font-weight:400">Quick contact</h3>

  <div class="abs col-panel" style="left:74px"></div>
  <div class="abs col-panel" style="left:279px"></div>
  <div class="abs col-panel" style="left:484px"></div>

  <article class="abs tweet-card">
    <div class="handle">Nora Lindell <span>@noralindell</span></div>
    <p>Nulla tincidunt elit a mauris pulvinar molestie. Maecenas vel nunc vitae dui mollis auctor. Proin in dolor eu urna sagittis fring illa. <a>Nulla suscipit lacus arcu</a>, ac rutrum tellus feugiat sit amet. Ut dictum, quam nec euismod.</p>
  </article>
  <div class="abs tweet-actions"><span>&#8617; Reply</span><span>&#8645; Retweet</span><span>&#9733; Favorite</span><span>&#8226;&#8226;&#8226; More</span></div>
  <div class="abs compose">Compose new post</div>

  <div class="abs blog-item" style="top:870px">
    <div class="blog-thumb" style="background:linear-gradient(90deg,#5a3a2a,#d8d0c8,#6a4a3a)" role="img" aria-label="Couple at the altar"></div>
    <p class="blog-text">Vivamus lobortis sagittis lacus, luctus viverra nunc dignissim<time>May-3-2014</time></p>
  </div>
  <div class="abs blog-item" style="top:926px">
    <div class="blog-thumb" style="background:linear-gradient(180deg,#9ac0e0,#e8eef4 60%,#d0d4c8)" role="img" aria-label="Couple on a beach with bouquet"></div>
    <p class="blog-text">Vivamus lobortis sagittis lacus, luctus viverra nunc dignissim<time>May-3-2014</time></p>
  </div>
  <div class="abs blog-item" style="top:982px">
    <div class="blog-thumb" style="background:linear-gradient(180deg,#a8b080,#6a7a4a 60%,#4a5a30)" role="img" aria-label="Wedding party group outdoors"></div>
    <p class="blog-text">Vivamus lobortis sagittis lacus, luctus viverra nunc dignissim<time>May-3-2014</time></p>
  </div>

  <form>
    <div class="abs field" style="top:877px">Name</div>
    <div class="abs field" style="top:902px">E-mail</div>
    <div class="abs field" style="top:927px">Phone</div>
    <div class="abs field" style="top:951px;height:40px">Comment</div>
    <div class="abs submit">SUBMIT</div>
  </form>
</section>

<section>
  <div class="abs info"></div>
  <svg class="abs info-icon" style="left:74px" width="14" height="16" viewBox="0 0 14 16"><rect x="1" y="1" width="12" height="14" fill="none" stroke="#777" stroke-width="1.5"/><rect x="4" y="4" width="2" height="2" fill="#777"/><rect x="8" y="4" width="2" height="2" fill="#777"/><rect x="4" y="8" width="2" height="2" fill="#777"/><rect x="8" y="8" width="2" height="2" fill="#777"/><rect x="5.5" y="11" width="3" height="4" fill="#777"/></svg>
  <div class="abs info-item" style="left:96px">55, Building name, streetname<br>City - Zip code</div>
  <svg class="abs info-icon" style="left:242px" width="16" height="16" viewBox="0 0 16 16"><path d="M3 1 L6 4 L4.5 6 Q7 10 10 11.5 L12 10 L15 13 L12.5 15.5 Q5 14 0.5 3.5 Z" fill="#777"/></svg>
  <div class="abs info-item" style="left:266px;top:1079px">Phone: 555 012 3478</div>
  <svg class="abs info-icon" style="left:387px" width="17" height="16" viewBox="0 0 17 16"><rect x="1" y="5" width="15" height="10" fill="#777"/><rect x="4" y="1" width="9" height="5" fill="none" stroke="#777" stroke-width="1.2"/><rect x="4" y="8" width="9" height="1.5" fill="#f4f4f4"/><rect x="4" y="11" width="9" height="1.5" fill="#f4f4f4"/></svg>
  <div class="abs info-item" style="left:412px;top:1079px">Fax : 555 012 3479</div>
  <svg class="abs info-icon" style="left:510px;top:1079px" width="16" height="11" viewBox="0 0 16 11"><rect x="0" y="0" width="16" height="11" fill="#777"/><polyline points="0,0 8,6 16,0" fill="none" stroke="#f4f4f4" stroke-width="1"/></svg>
  <div class="abs info-item" style="left:534px;top:1079px">E-mail : info@maplehollownc.com</div>
</section>

<footer>
  <div class="abs footer"></div>
  <span class="abs foot-link" style="left:124px">&#8226; Home</span>
  <span class="abs foot-link" style="left:193px">&#8226; Wedding Venues</span>
  <span class="abs foot-link" style="left:304px">&#8226; Reception Venues</span>
  <span class="abs foot-link" style="left:420px">&#8226; About US</span>
  <span class="abs foot-link" style="left:501px">&#8226; Contact US</span>
  <span class="abs foot-link" style="left:589px">&#8226; Blog</span>
  <div class="abs foot-rule"></div>
  <p class="abs copyright">Copyright &copy; 2014 Maple Hollow Nuptial Company. &nbsp;All rights reserved.</p>
  <span class="abs social" style="left:572px" aria-label="Social link"></span>
  <span class="abs social" style="left:599px" aria-label="Social link"></span>
  <span class="abs social" style="left:627px" aria-label="Social link"></span>
  <span class="abs social" style="left:654px" aria-label="Social link"></span>
</footer>

</body>
</html>
```